Business Card Design

We need a business card design for a Non-Profit Christian Based Organization located in Milford, Pa.
Alder Ridge Helping Harbor
Is a Christ-centered organization dedicated to providing compassion and hope to homeless or near homeless, families and individuals, by meeting their basic and urgent need of food, clothing and shelter.
Updates
the logo is black and white
and must add the color green some where 00400
Industry/Entity Type
Clothing
Contact Information for Business Card
Alder Ridge Helping Harbor
P.O. Box 287
Fernvale, Pa 18290
Phone: (570) 413-CARE(2273)
Toll Free: (855) 413-CARE
email:Info@alderridgehh.org
email:Careline@alderridgehh.org
Our organization already has a logo.
Front of card:
Is a Christ-centered organization dedicated to providing compassion and hope to homeless or near homes, families and individual by meeting their basic and urgent need of food, clothing and shelter.(this is our Mission Statement)
On back of card:
'I was hungry and you gave me something to eat;
"I was thirsty and you gave me something to drink;
"I was a stranger and you invited me in."
Matthew 25:35
Color: Logo is black and white
Background color I would like a bright light green 00ff00(close to that)
I attached a sample of what I created on Quill Press but, I don't like the color green, nor the design (but I just wanted to give you and Idea of the Logo and Alder Ridge (one line) Helping Harbor (second line) in a different font thank you
Delia Rostova
Pr/Board of Directors

```html
<!DOCTYPE html>
<html lang="en">
<head>
<meta charset="utf-8">
<title>Alder Ridge Helping Harbor – Business Card</title>
<link rel="stylesheet" href="https://fonts.googleapis.com/css2?family=Barlow+Condensed:ital,wght@1,400&family=Open+Sans:ital,wght@0,700;1,400&family=Source+Sans+3:ital,wght@0,700;1,600;1,700&display=swap">
<style>
  :root {
    --leaf: #98c23a;
    --leaf-dark: #6f9a3c;
    --band-light: #aad530;
    --band-edge: #6e9a3d;
    --paper: #ffffff;
    --ink: #111111;
    --frame: #2a2a22;
  }
  * { margin: 0; padding: 0; box-sizing: border-box; }
  html, body { width: 1024px; height: 1200px; overflow: hidden; background: var(--paper); }
  .card { position: relative; width: 1024px; height: 1200px; background: var(--paper); }

  .org-title {
    position: absolute; top: 48px; left: 0; width: 100%;
    text-align: center; color: var(--leaf);
    font: italic 700 57px/1 "Source Sans 3", sans-serif; letter-spacing: -0.5px;
  }
  .mission {
    position: absolute; top: 121px; left: 30px; width: 964px;
    text-align: center; color: var(--leaf);
    font: italic 400 33px/43px "Barlow Condensed", sans-serif;
  }

  .band {
    position: absolute; left: 0; width: 100%;
    background: radial-gradient(ellipse at center, var(--band-light) 0%, #9fcb32 45%, var(--band-edge) 100%);
  }
  .band-contact { top: 258px; height: 342px; }
  .band-sign { top: 831px; height: 369px; }

  .mark-tile {
    position: absolute; background: var(--paper);
    border: 4px solid var(--frame); border-radius: 8px;
    box-shadow: 2px 3px 6px rgba(0,0,0,0.35);
    display: flex; align-items: center; justify-content: center; text-align: center;
  }
  .mark-name {
    color: var(--ink); font: 700 30px/1.1 "Source Sans 3", sans-serif;
  }
  .band-contact .mark-tile { left: 142px; top: 10px; width: 182px; height: 272px; }
  .band-sign .mark-tile { left: 440px; top: 10px; width: 145px; height: 216px; }
  .band-sign .mark-name { font-size: 25px; }

  .contact {
    position: absolute; left: 369px; top: 9px; color: var(--paper);
    font: 700 26px/38px "Open Sans", sans-serif; letter-spacing: 0.5px;
    text-shadow: 1px 2px 3px rgba(0,0,0,0.45);
  }
  .contact p + p { margin-top: 23px; }
  .contact .label { font-style: italic; font-weight: 400; }

  .verse {
    position: absolute; top: 645px; left: 0; width: 100%;
    text-align: center; color: var(--leaf);
    font: italic 600 38px/47px "Source Sans 3", sans-serif;
  }
  .verse-ref {
    position: absolute; top: 796px; left: 0; width: 100%;
    text-align: center; color: var(--leaf-dark);
    font: 700 27px/1 "Source Sans 3", sans-serif;
  }

  .sign-name {
    position: absolute; top: 236px; left: 0; width: 100%;
    text-align: center; color: var(--paper);
    font: italic 700 38px/1 "Source Sans 3", sans-serif;
    text-shadow: 1px 2px 3px rgba(0,0,0,0.45);
  }
  .sign-thanks {
    position: absolute; top: 290px; left: 0; width: 100%;
    text-align: center; color: var(--paper);
    font: italic 700 21px/1 "Source Sans 3", sans-serif;
    text-shadow: 1px 2px 3px rgba(0,0,0,0.45);
  }
</style>
</head>
<body>
<main class="card">
  <h1 class="org-title">Alder Ridge Helping Harbor</h1>
  <p class="mission">Is a Christ-centered organization dedicated to providing compassion and hope to<br>homeless or near homes, families and individual by meeting their basic and<br>urgent need of food, clothing and shelter.</p>

  <section class="band band-contact">
    <div class="mark-tile"><span class="mark-name">Helping<br>Harbor</span></div>
    <div class="contact">
      <p>P.O. Box 287<br>Fernvale, Pa 18290</p>
      <p><span class="label">Phone:</span> (570) 413-CARE(2273)<br><span class="label">Toll Free:</span> (855) 413-CARE(2273)</p>
      <p><span class="label">Email:</span> Info@alderridgehh.org<br><span class="label">Email:</span> Careline@alderridgehh.org</p>
    </div>
  </section>

  <blockquote class="verse">“I was hungry and you gave me something to eat;<br>I was thirsty and you gave me something to drink;<br>I was a stranger and you invited me in."</blockquote>
  <p class="verse-ref">Matthew 25:35</p>

  <section class="band band-sign">
    <div class="mark-tile"><span class="mark-name">Helping<br>Harbor</span></div>
    <p class="sign-name">Helping Harbor</p>
    <p class="sign-thanks">Thank you Delia Rostova Pr/Board of Directors</p>
  </section>
</main>
</body>
</html>
```